Professional business cards for real estate development company

I need business cards for my new real estate development company. The company, "KORVA" is a real estate development, investment, and advisory firm with a focus on multifamily, office, and mixed-use projects across primary and secondary markets in the Southeast United States.

Style preference is modern

Industry/Entity Type

Real Estate Development

Contact Information for Business Card

The business cards need to include:
Name
Title
Mailing Address
Phone Number
Web Address

Logo is attached. I would like white to be the primary color with incorporation of the company colors: #232D3A and #B5A451

Font styles to use
Other font styles liked:
• Montserrat, Avenir

Requirements
Must have
• Company Logo. No need to include the company name since the name is in the logo.
Should not have
• No line type designs

```html
<!DOCTYPE html>
<html lang="en">
<head>
<meta charset="utf-8">
<title>KORVA Business Card</title>
<link href="https://fonts.googleapis.com/css2?family=Lato:wght@400;700&display=swap" rel="stylesheet">
<style>
  :root {
    --page-bg: #e8e3db;
    --card-bg: #f4f2ee;
    --card-edge: #ffffff;
    --gold: #b5a451;
    --gold-light: #cfbf72;
    --navy: #232d3a;
    --navy-soft: #3a434f;
    --ink: #353b42;
    --cream: #f5f1e6;
    --title-tone: #efe6c4;
  }
  * { box-sizing: border-box; margin: 0; padding: 0; }
  html, body {
    width: 1200px;
    height: 1047px;
    overflow: hidden;
    background: var(--page-bg);
    font-family: "Lato", sans-serif;
  }
  .business-card {
    position: absolute;
    left: 80px;
    top: 241px;
    width: 1040px;
    height: 565px;
    border-radius: 26px;
    background: var(--card-bg);
    border: 2px solid var(--card-edge);
    box-shadow: 0 18px 40px rgba(35, 45, 58, 0.12);
    overflow: hidden;
  }
  .identity-panel {
    position: absolute;
    left: 0;
    top: 0;
    width: 500px;
    height: 274px;
    border-radius: 0 0 20px 0;
    background: linear-gradient(135deg, var(--gold) 0%, var(--gold-light) 100%);
  }
  .person-name {
    position: absolute;
    left: 74px;
    top: 102px;
    font-size: 46px;
    font-weight: 700;
    letter-spacing: 0.5px;
    color: var(--ink);
  }
  .person-title {
    position: absolute;
    left: 74px;
    top: 164px;
    font-size: 25px;
    font-weight: 400;
    color: var(--title-tone);
  }
  .contact-panel {
    position: absolute;
    left: 0;
    top: 288px;
    width: 496px;
    height: 277px;
    border-radius: 0 20px 0 0;
    background: linear-gradient(135deg, var(--navy-soft) 0%, var(--navy) 100%);
    color: var(--cream);
  }
  .mailing-address {
    position: absolute;
    left: 66px;
    top: 44px;
    font-size: 26px;
    line-height: 34px;
  }
  .contact-list {
    position: absolute;
    left: 66px;
    top: 128px;
    list-style: none;
  }
  .contact-item {
    display: flex;
    align-items: center;
    height: 38px;
    font-size: 26px;
  }
  .contact-icon {
    width: 26px;
    height: 26px;
    margin-right: 24px;
    flex: none;
  }
  .brand-mark {
    position: absolute;
    left: 530px;
    top: 0;
    width: 510px;
    height: 565px;
    display: flex;
    align-items: center;
    justify-content: center;
  }
  .brand-name {
    font-size: 84px;
    font-weight: 700;
    letter-spacing: 6px;
    color: var(--navy);
  }
</style>
</head>
<body>
  <div class="business-card">
    <div class="identity-panel">
      <div class="person-name">EVAN HARLOW</div>
      <div class="person-title">Founder &amp; CEO</div>
    </div>

    <div class="contact-panel">
      <div class="mailing-address">
        1234 First Line Address<br>
        5678 Second Line Address
      </div>
      <ul class="contact-list">
        <li class="contact-item">
          <svg class="contact-icon" viewBox="0 0 24 24" aria-hidden="true">
            <path d="M6.6 10.8a15 15 0 0 0 6.6 6.6l2.2-2.2a1 1 0 0 1 1-.25 11.4 11.4 0 0 0 3.6.57 1 1 0 0 1 1 1V20a1 1 0 0 1-1 1A17 17 0 0 1 3 4a1 1 0 0 1 1-1h3.5a1 1 0 0 1 1 1c0 1.25.2 2.45.57 3.6a1 1 0 0 1-.25 1z" fill="var(--gold)"/>
          </svg>
          4045550182
        </li>
        <li class="contact-item">
          <svg class="contact-icon" viewBox="0 0 24 24" aria-hidden="true">
            <rect x="2" y="5" width="20" height="14" rx="1" fill="var(--gold)"/>
            <path d="M2.5 5.5 12 13l9.5-7.5" fill="none" stroke="var(--navy)" stroke-width="1.6"/>
          </svg>
          info@korvadev.com
        </li>
        <li class="contact-item">
          <svg class="contact-icon" viewBox="0 0 24 24" aria-hidden="true">
            <g fill="none" stroke="var(--gold)" stroke-width="1.6">
              <circle cx="12" cy="12" r="9"/>
              <ellipse cx="12" cy="12" rx="4" ry="9"/>
              <path d="M3 12h18M4.5 7.5h15M4.5 16.5h15"/>
            </g>
          </svg>
          www.korvadev.com
        </li>
      </ul>
    </div>

    <div class="brand-mark">
      <span class="brand-name">KORVA</span>
    </div>
  </div>
</body>
</html>
```